High Tech Real Estate Startup needs a business card

We are developing an innovative real estate marketing product based around advanced search and virtual reality.

We talk to people, we need business cards.

Target Market(s)

The target market is technology professionals and realtors.

Contact Information for Business Card

The information to be included will include

Name
Title
Phone Number
E-mail Address
www.plindo.com

It should use simple iconography for each one of those fields.

Font styles to use
Other font styles liked:
• Co, Jubilat, Avenir

Colors

Designer to choose colors to be used in the design.

Requirements
Must have
• Clean aesthetic,
• Good use of negative space.
• It should use our company logo, shown in the attached file. It is able to use the negative of that logo (coloured font and white background) and I have attached other acceptable accent colours in a swatch file.
Should not have
• Should not be too busy
• No extraneous text (slogans, tag lines etc)

```html
<!DOCTYPE html>
<html lang="en">
<head>
<meta charset="utf-8">
<title>Plindo Business Card</title>
<link href="https://fonts.googleapis.com/css2?family=Figtree:wght@400;500;600&display=swap" rel="stylesheet">
<style>
  :root {
    --teal: #17b8bb;
    --ink: #555555;
    --rule: #b5b5b5;
    --paper: #fbfbfb;
    --backdrop: #d9d9d9;
  }
  * { margin: 0; padding: 0; box-sizing: border-box; }
  html, body {
    width: 1200px;
    height: 1134px;
    overflow: hidden;
    background: var(--backdrop);
    font-family: "Figtree", sans-serif;
    color: var(--ink);
  }
  .card {
    position: absolute;
    left: 261px;
    width: 675px;
    height: 382px;
    background: var(--paper);
    box-shadow: 0 2px 6px rgba(0,0,0,0.25);
  }
  .card--front { top: 161px; }
  .card--back { top: 590px; }

  .brand {
    position: absolute;
    display: flex;
    align-items: center;
    gap: 12px;
    color: var(--teal);
    font-weight: 600;
    letter-spacing: 0.5px;
    white-space: nowrap;
  }
  .brand__mark { display: block; background: var(--teal); flex: none; }
  .card--front .brand { left: 46px; top: 108px; font-size: 26px; line-height: 32px; }
  .card--front .brand__mark { width: 28px; height: 28px; }
  .card--back .brand {
    left: 0; right: 0; top: 166px;
    justify-content: center;
    font-size: 32px; line-height: 40px; gap: 14px;
  }
  .card--back .brand__mark { width: 34px; height: 34px; }

  .person {
    position: absolute;
    right: 44px;
    top: 200px;
    text-align: right;
  }
  .person__name { color: var(--teal); font-size: 29px; font-weight: 500; line-height: 34px; }
  .person__title { font-size: 20px; line-height: 24px; }

  .divider {
    position: absolute;
    left: 46px;
    top: 271px;
    width: 585px;
    height: 2px;
    background: var(--rule);
  }
  .contact {
    position: absolute;
    left: 46px;
    display: flex;
    align-items: center;
    gap: 10px;
    font-size: 17.5px;
    line-height: 20px;
  }
  .contact--phone { top: 287px; }
  .contact--email { top: 314px; }
  .contact svg { width: 17px; height: 17px; fill: var(--teal); }

  .website { font-size: 17px; line-height: 20px; }
  .website em { font-style: normal; color: var(--teal); }
  .card--front .website { position: absolute; right: 44px; top: 314px; }
  .card--back .website { position: absolute; left: 0; right: 0; top: 324px; text-align: center; }
</style>
</head>
<body>
  <section class="card card--front">
    <div class="brand"><span class="brand__mark"></span><span>PLINDO</span></div>
    <div class="person">
      <div class="person__name">Daniel Reyes</div>
      <div class="person__title">President</div>
    </div>
    <div class="divider"></div>
    <div class="contact contact--phone">
      <svg viewBox="0 0 24 24" aria-hidden="true"><path d="M6.6 10.8c1.4 2.8 3.8 5.1 6.6 6.6l2.2-2.2c.3-.3.7-.4 1-.2 1.1.4 2.3.6 3.6.6.6 0 1 .4 1 1V20c0 .6-.4 1-1 1C10.6 21 3 13.4 3 4c0-.6.4-1 1-1h3.5c.6 0 1 .4 1 1 0 1.3.2 2.5.6 3.6.1.3 0 .7-.2 1z"/></svg>
      <span>555 014 2286</span>
    </div>
    <div class="contact contact--email">
      <svg viewBox="0 0 24 24" aria-hidden="true"><path d="M2 5h20v2l-10 6L2 7z"/><path d="M2 9l10 6 10-6v10H2z"/></svg>
      <span>info@plindo.com</span>
    </div>
    <div class="website">www.<em>plindo</em>.com</div>
  </section>

  <section class="card card--back">
    <div class="brand"><span class="brand__mark"></span><span>PLINDO</span></div>
    <div class="website">www.<em>plindo</em>.com</div>
  </section>
</body>
</html>
```